terras letterhead

We would like to create a new letterhead that our company will use for proposals, invoices, statements and letters. Our company name is Terra-Crafters. We are a landscape design/build and landscape maintenance company. We have a web site Terra-Crafters.example where our logo (the leaf with the lettering within it only) is displayed.

Industry/Entity Type

Graphic Design

Requirements
Must have
• Address and info on our current letterhead (uploaded)
Nice to have
• We would like the design to look presentable in grey scale as well as color.
Should not have
• Do not want to infringe much on the normal useable area within the normal print areas.

```html
<!DOCTYPE html>
<html lang="en">
<head>
<meta charset="utf-8">
<title>Terra-Crafters Letterhead</title>
<link rel="stylesheet" href="https://fonts.googleapis.com/css2?family=Noto+Serif:wght@700&display=swap">
<style>
  :root {
    --backdrop: #5a5b5d;
    --paper: #ffffff;
    --watermark: #f4f4f4;
    --brand-green: #1f4a2a;
    --ink: #2a2410;
    --rule: #3b3a14;
  }
  html, body {
    margin: 0;
    padding: 0;
    width: 1200px;
    height: 1000px;
    overflow: hidden;
    background: var(--backdrop);
  }
  .letterhead {
    position: absolute;
    left: 294px;
    top: 85px;
    width: 601px;
    height: 845px;
    background: var(--paper);
    font-family: "Noto Serif", Georgia, serif;
    font-weight: 700;
  }
  .watermark-field {
    position: absolute;
    inset: 0;
    background: linear-gradient(180deg, var(--watermark), #f8f8f8 50%, var(--watermark));
  }
  .brand-name {
    position: absolute;
    left: 0;
    right: 0;
    top: 34px;
    text-align: center;
    font-size: 14px;
    letter-spacing: 0.5px;
    color: var(--brand-green);
    margin: 0;
  }
  .contact-block {
    position: absolute;
    left: 0;
    right: 0;
    top: 70px;
    text-align: center;
    font-size: 11px;
    line-height: 15px;
    color: var(--ink);
    margin: 0;
  }
  .rule {
    position: absolute;
    left: 60px;
    width: 481px;
    height: 1.5px;
    background: var(--rule);
  }
  .rule-top { top: 101px; }
  .rule-bottom { top: 815px; }
</style>
</head>
<body>
  <div class="letterhead">
    <div class="watermark-field" role="img" aria-label="Faint repeating leaf watermark pattern across the page"></div>
    <p class="brand-name">Terra-Crafters</p>
    <p class="contact-block">
      Phone: (555) 014-2208 | Fax: (555) 014-2290 | Email: service@terra-crafters.example<br>
      Web: terra-crafters.example | 1250 Meadowbrook Avenue Cedar Hollow, NJ 07000
    </p>
    <div class="rule rule-top"></div>
    <div class="rule rule-bottom"></div>
  </div>
</body>
</html>
```